I am looking for a modern, clean and neat design for a reflexology and well being business. The business name is Mira Tellus (this is an old Latin word for wellbeing). The colours I would like are purple, white and grey. I am open to suggestions for pictures such as healing or working hands, a pair of feet, images that represent my business that you may think of....... or maybe you think no images at all would be best? My tag line is: "Relax, Renew, Revive" or "Find you balance......... Relax, Renew, Revive" I can decide which I want so I would like to see what both would look like. I would like space on the back to write the client's appointment date and time (more than once)

```html
<!DOCTYPE html>
<html lang="en">
<head>
<meta charset="utf-8">
<title>Mira Tellus – Business Cards</title>
<link href="https://fonts.googleapis.com/css2?family=Open+Sans:wght@300;400;600;700&display=swap" rel="stylesheet">
<style>
  :root {
    --backdrop: #b9b7bf;
    --card: #3d2656;
    --card-deep: #2c1a40;
    --ink: #ffffff;
    --ink-soft: #d8cfe3;
    --accent: #c9b6e4;
    --rule: #e6e1ec;
  }
  * { box-sizing: border-box; margin: 0; padding: 0; }
  html, body { width: 1200px; height: 900px; overflow: hidden; }
  body {
    background: var(--backdrop);
    font-family: "Open Sans", Arial, sans-serif;
    color: var(--ink);
  }
  .canvas { position: relative; width: 1200px; height: 900px; }
  .card {
    position: absolute;
    width: 540px;
    height: 310px;
    background: linear-gradient(160deg, var(--card), var(--card-deep));
    border-radius: 22px;
    box-shadow: 0 18px 40px rgba(40,30,55,0.35);
    overflow: hidden;
  }
  .card--appointment { left: 40px; top: 110px; }
  .card--contact { left: 620px; top: 480px; }

  .brand-mark {
    position: absolute;
    border-radius: 50%;
    border: 3px solid var(--ink);
  }
  .brand-name {
    position: absolute;
    font-weight: 300;
    font-size: 17px;
    letter-spacing: 0.5px;
    text-transform: uppercase;
    white-space: nowrap;
  }

  /* appointment side */
  .card--appointment .brand-mark { left: 190px; top: 26px; width: 54px; height: 54px; }
  .card--appointment .brand-name { left: 164px; top: 88px; }
  .tagline {
    position: absolute;
    left: 262px;
    top: 30px;
    font-size: 12px;
    text-transform: uppercase;
    letter-spacing: 0.3px;
  }
  .appointment {
    position: absolute;
    left: 34px;
    top: 128px;
    width: 440px;
  }
  .appointment__title { font-weight: 700; font-size: 17px; margin-bottom: 2px; }
  .appointment__row {
    display: flex;
    align-items: flex-end;
    height: 28px;
    font-size: 13px;
    padding-left: 22px;
    gap: 4px;
  }
  .appointment__row .fill {
    flex: 1;
    border-bottom: 1.5px dotted var(--ink-soft);
    margin-bottom: 4px;
  }
  .appointment__row .label + .fill + .label { margin-left: 10px; }

  /* contact side */
  .rule { position: absolute; height: 1.5px; background: var(--rule); }
  .rule--top { left: 250px; right: 22px; top: 34px; }
  .rule--bottom { left: 22px; width: 300px; bottom: 26px; }
  .card--contact .brand-mark { left: 200px; top: 62px; width: 62px; height: 62px; }
  .card--contact .brand-name { left: 180px; top: 144px; }

  .person { position: absolute; left: 34px; bottom: 44px; }
  .person__name {
    font-weight: 700;
    font-size: 21px;
    letter-spacing: 0.6px;
    text-transform: uppercase;
    line-height: 1.1;
  }
  .person__role {
    font-size: 12px;
    color: var(--accent);
    letter-spacing: 1px;
    text-transform: uppercase;
    padding-left: 70px;
  }
  .contact-list {
    position: absolute;
    left: 300px;
    top: 196px;
    list-style: none;
    font-size: 13px;
    line-height: 1.35;
  }
  .contact-list li { display: flex; align-items: center; gap: 7px; }
  .contact-list svg { width: 10px; height: 10px; flex: none; }
</style>
</head>
<body>
<main class="canvas">

  <section class="card card--appointment" aria-label="Appointment card">
    <span class="brand-mark" aria-hidden="true"></span>
    <span class="brand-name">Mira Tellus</span>
    <p class="tagline">Relax, Renew, Revive</p>

    <div class="appointment">
      <p class="appointment__title">Appointment:</p>
      <div class="appointment__row"><span class="label">Name:</span><span class="fill"></span></div>
      <div class="appointment__row"><span class="label">Date:</span><span class="fill"></span><span class="label">Time:</span><span class="fill"></span></div>
      <div class="appointment__row"><span class="label">Date:</span><span class="fill"></span><span class="label">Time:</span><span class="fill"></span></div>
      <div class="appointment__row"><span class="label">Date:</span><span class="fill"></span><span class="label">Time:</span><span class="fill"></span></div>
    </div>
  </section>

  <section class="card card--contact" aria-label="Contact card">
    <span class="rule rule--top"></span>
    <span class="brand-mark" aria-hidden="true"></span>
    <span class="brand-name">Mira Tellus</span>

    <div class="person">
      <p class="person__name">Alden Crowe</p>
      <p class="person__role">Director</p>
    </div>

    <ul class="contact-list">
      <li>
        <svg viewBox="0 0 10 10" aria-hidden="true"><path d="M2 1 L4 1 L4.6 3 L3.5 3.8 Q4.5 5.8 6.2 6.5 L7 5.4 L9 6 L9 8 Q8.5 9 7.5 9 Q1 8 1 2.5 Q1 1.2 2 1Z" fill="#ffffff"/></svg>
        +330 5172-9034
      </li>
      <li>
        <svg viewBox="0 0 10 10" aria-hidden="true"><rect x="0.5" y="2" width="9" height="6" fill="none" stroke="#ffffff" stroke-width="1"/><path d="M0.5 2 L5 5.5 L9.5 2" fill="none" stroke="#ffffff" stroke-width="1"/></svg>
        hello@miratellus.com
      </li>
      <li>
        <svg viewBox="0 0 10 10" aria-hidden="true"><circle cx="5" cy="5" r="4.3" fill="none" stroke="#ffffff" stroke-width="1"/><ellipse cx="5" cy="5" rx="1.8" ry="4.3" fill="none" stroke="#ffffff" stroke-width="0.8"/><path d="M0.7 5 H9.3" stroke="#ffffff" stroke-width="0.8"/></svg>
        www.miratellus.com
      </li>
    </ul>
    <span class="rule rule--bottom"></span>
  </section>

</main>
</body>
</html>
```